Artwork for New Single, ”Hold Fire”

Unique design describing Silence.
Use the pictures provided for ideas.
Looking for something out the box, different.
Make this stand out. Modern times or futuristic.
Imagination welcomed.
GRAVEL ENTERTAINMENT INC.
Artist name is Gravel
Song Title: Hold Fire

Target Market(s)

Millennials, Trap music listeners, Hardcore rap fans.

Colors

Designer to choose colors to be used in the design.

Requirements
Nice to have
• Bold, serious designs. Make a statement. Masculine, professional in nature.

```html
<!DOCTYPE html>
<html lang="en">
<head>
<meta charset="utf-8">
<title>Gravel – Hold Fire</title>
<link rel="stylesheet" href="https://fonts.googleapis.com/css2?family=Archivo:wdth,wght@125,900&family=Bungee&family=Arimo&display=swap">
<style>
  :root {
    --ink: #000000;
    --paper: #ffffff;
    --sky-light: #dcf2f7;
    --sky: #a9dbe2;
    --ember: #e0441a;
    --ember-soft: #f08a5c;
  }
  html, body {
    margin: 0;
    padding: 0;
    width: 1051px;
    height: 1200px;
    overflow: hidden;
    background: var(--ink);
  }
  .cover {
    position: relative;
    width: 1051px;
    height: 1200px;
    background: var(--ink);
  }
  .cover-art {
    position: absolute;
    left: 45px;
    top: 40px;
    width: 962px;
    height: 962px;
    overflow: hidden;
    background:
      radial-gradient(ellipse 38% 48% at 49% 52%, var(--ember) 0%, var(--ember-soft) 45%, rgba(240,138,92,0) 80%),
      linear-gradient(180deg, var(--sky-light) 0%, var(--sky) 100%);
  }
  .artist-name {
    position: absolute;
    right: 80px;
    top: 70px;
    margin: 0;
    font-family: "Archivo", "Arial Black", sans-serif;
    font-stretch: 125%;
    font-weight: 900;
    font-size: 60px;
    line-height: 1;
    letter-spacing: 1px;
    color: var(--ink);
  }
  .song-title {
    position: absolute;
    left: 239px;
    top: 800px;
    width: 573px;
    height: 150px;
    overflow: visible;
  }
  .song-title text {
    font-family: "Bungee", "Impact", sans-serif;
    font-size: 176px;
    fill: var(--ink);
  }
  .draft-note {
    position: absolute;
    left: 674px;
    top: 1063px;
    width: 377px;
    height: 85px;
    box-sizing: border-box;
    padding: 7px 0 0 11px;
    background: var(--paper);
    font-family: "Arimo", "Arial", sans-serif;
    font-size: 18.5px;
    line-height: 22px;
    color: var(--ink);
  }
  .draft-note p { margin: 0; }
</style>
</head>
<body>
  <main class="cover">
    <div class="cover-art" role="img" aria-label="Photo of a red and white French bulldog puppy with a finger raised to its nose in a hush gesture, on a pale blue background"></div>
    <h1 class="artist-name">GRAVEL</h1>
    <svg class="song-title" viewBox="0 0 573 150" aria-label="Hold Fire">
      <text x="0" y="140" textLength="573" lengthAdjust="spacingAndGlyphs">HOLD FIRE</text>
    </svg>
    <div class="draft-note">
      <p>DRAFT 1:</p>
      <p>First version for proof of concept</p>
      <p>for the 1st round of feedback</p>
    </div>
  </main>
</body>
</html>
```